New Graphic Design Project / Email signiture and Letterhead

I would like a new SIMPLE but high end quality modern/heavy industrial design for an email Signiture and letter head that incorporates product photos or illustrations of our products to show our customers our range of products and also show our head office in Perth Western Australia and also our Australian and international reseller locations.
in my present email signature you would see that I have other company logos these companies are old partners of ours but some are no longer so I would like to have the option to add and change them if things change in the future.
for ideas Our main products are as follows
Composite Hose
Convoluted hose
Metal expansion joints
Fabric expansion joints
Rubber Expansion joints
Please see our website for ideas and our product photos.
www.brovantec.com.au
if you need any further information please let me know
i have attached our old email signiture for reference.
Declan

Target Market(s)

Oil and Gas / Mining / Petroleum and Chemical Refineries, high end engineering

Requirements
Must have
• pictures / photos of our core products and our company capabilities to show our existing and new customers what we can do.
in the email signature - links to company face book and LinkedIn, our website
I would like to have spaces for my company partners logos and need the final file to be in a format for me to change and update all details
All so our Font is Conthrax SB
Nice to have
• the email signature, I would like this to have all the required information ( as per attached present email signature ) but also be informative / marketing to show customers what we do if possible.
the letter head can be based from the same but simple with or without product photos

```html
<!DOCTYPE html>
<html lang="en">
<head>
<meta charset="utf-8">
<title>Brovantec Letterhead</title>
<link rel="stylesheet" href="https://fonts.googleapis.com/css2?family=Source+Sans+3:wght@400;700&display=swap">
<style>
  :root {
    --charcoal: #4d4b4d;
    --steel: #a9a9ac;
    --steel-light: #bdbdc0;
    --panel: #d2d2d5;
    --ink: #4a4a4c;
    --navy: #0e1030;
    --white: #ffffff;
  }
  * { margin: 0; padding: 0; box-sizing: border-box; }
  html, body { width: 848px; height: 1200px; overflow: hidden; background: var(--white); }
  .letterhead {
    position: relative; width: 848px; height: 1200px; overflow: hidden;
    font-family: "Source Sans 3", "Source Sans Pro", sans-serif; color: var(--ink);
    background: var(--white);
  }
  .frame { position: absolute; inset: 0; }
  .brand {
    position: absolute; top: 31px; right: 40px;
    display: flex; align-items: center; gap: 14px;
  }
  .brand-dot {
    width: 54px; height: 54px; border-radius: 50%;
    border: 6px solid var(--charcoal);
  }
  .brand-name {
    font-size: 32px; font-weight: 700; letter-spacing: 1px; color: #2c2c2e;
  }
  .industry-scene {
    position: absolute; left: 90px; right: 0; top: 820px; height: 243px;
    background:
      linear-gradient(180deg, rgba(255,255,255,1) 0%, rgba(255,255,255,0) 35%),
      linear-gradient(90deg, #f4f4f6 0%, #f2efe6 30%, #eceef1 60%, #e6e9ec 100%);
  }
  .contact-list { position: absolute; left: 100px; top: 866px; list-style: none; }
  .contact-list li {
    height: 43px; line-height: 32px; font-size: 18.5px; white-space: nowrap;
  }
  .contact-list strong { font-weight: 700; }
  .product-band {
    position: absolute; left: 0; top: 1063px; width: 848px; height: 29px;
    background: var(--navy); color: var(--white);
    font-weight: 700; font-size: 17px; line-height: 29px; text-align: center; white-space: nowrap;
  }
  .product-band .sep { font-size: 10px; vertical-align: 2px; padding: 0 3px; }
  .product-strip { position: absolute; left: 0; top: 1092px; width: 848px; height: 108px; }
</style>
</head>
<body>
<div class="letterhead">
  <div class="industry-scene" role="img" aria-label="Faint photo of a refinery skyline with chimneys and towers"></div>

  <svg class="frame" width="848" height="1200" viewBox="0 0 848 1200" aria-hidden="true">
    <polygon points="0,388 51,417 51,505 0,476" fill="var(--steel-light)"/>
    <polygon points="0,476 51,505 51,594 0,565" fill="var(--steel)"/>
    <polygon points="0,565 51,594 51,685 0,656" fill="var(--steel-light)"/>
    <rect x="51" y="0" width="39" height="725" fill="var(--charcoal)"/>
    <polygon points="51,800 90,800 90,838 70,846 51,838" fill="var(--charcoal)"/>
    <polygon points="51,840 70,848 90,840 90,1040 70,1048 51,1040" fill="var(--panel)" stroke="var(--white)" stroke-width="2"/>
    <polygon points="51,1045 70,1053 90,1045 90,1063 51,1063" fill="var(--charcoal)"/>
    <circle cx="70" cy="764" r="44" fill="var(--white)"/>
    <circle cx="70" cy="764" r="38" fill="none" stroke="var(--charcoal)" stroke-width="6"/>
    <!-- phone -->
    <rect x="63" y="871" width="15" height="25" rx="2" fill="none" stroke="var(--charcoal)" stroke-width="2.5"/>
    <circle cx="70.5" cy="892" r="1.3" fill="var(--charcoal)"/>
    <!-- globe -->
    <circle cx="70" cy="925" r="12" fill="none" stroke="var(--charcoal)" stroke-width="2.5"/>
    <ellipse cx="70" cy="925" rx="5" ry="12" fill="none" stroke="var(--charcoal)" stroke-width="2"/>
    <line x1="58" y1="925" x2="82" y2="925" stroke="var(--charcoal)" stroke-width="2"/>
    <line x1="60" y1="919" x2="80" y2="919" stroke="var(--charcoal)" stroke-width="1.6"/>
    <line x1="60" y1="931" x2="80" y2="931" stroke="var(--charcoal)" stroke-width="1.6"/>
    <!-- building -->
    <rect x="60" y="956" width="20" height="25" fill="var(--charcoal)"/>
    <g fill="var(--panel)">
      <rect x="64" y="960" width="3" height="3"/><rect x="73" y="960" width="3" height="3"/>
      <rect x="64" y="966" width="3" height="3"/><rect x="73" y="966" width="3" height="3"/>
      <rect x="68" y="974" width="4" height="7"/>
    </g>
    <!-- pin -->
    <path d="M70 1023 C64 1014 60 1009 60 1004 A10 10 0 0 1 80 1004 C80 1009 76 1014 70 1023 Z" fill="var(--charcoal)"/>
  </svg>

  <header class="brand">
    <span class="brand-dot"></span>
    <span class="brand-name">BROVANTEC</span>
  </header>

  <ul class="contact-list">
    <li>+614 55 210 384 | +618 92 417 650</li>
    <li>www.brovantec.com.au</li>
    <li><strong>Head Office:</strong> 42 Kelvin Street, Welshpool, WA 6106</li>
    <li><strong>Locations:</strong> Australia, Singapore, Indonesia, Vietnam</li>
  </ul>

  <div class="product-band">Composite Hose <span class="sep">◆</span> Rubber Expansion Joints <span class="sep">◆</span> Stainless Braided Hose <span class="sep">◆</span> Metallic Expansion Joints</div>

  <svg class="product-strip" width="848" height="108" viewBox="0 0 848 108">
    <defs>
      <linearGradient id="metal" x1="0" x2="1"><stop offset="0" stop-color="#c9ccd0"/><stop offset="0.6" stop-color="#7e8898"/><stop offset="1" stop-color="#d5d8dc"/></linearGradient>
      <linearGradient id="rubber" x1="0" x2="1"><stop offset="0" stop-color="#d9dadc"/><stop offset="0.5" stop-color="#2b2b2e"/><stop offset="1" stop-color="#8c8f94"/></linearGradient>
      <linearGradient id="braided" x1="0" x2="1"><stop offset="0" stop-color="#9aa6b0"/><stop offset="0.5" stop-color="#6f7a82"/><stop offset="1" stop-color="#a9b0b4"/></linearGradient>
      <linearGradient id="site" x1="0" x2="1"><stop offset="0" stop-color="#b3b0a8"/><stop offset="0.6" stop-color="#8e8b84"/><stop offset="1" stop-color="#6c8f52"/></linearGradient>
    </defs>
    <rect width="848" height="108" fill="var(--white)"/>
    <path d="M2 0 H165 Q180 55 195 108 H2 Z" fill="url(#metal)" role="img" aria-label="Photo of metallic expansion joints with blue flanges"/>
    <path d="M170 0 H380 Q390 55 405 108 H200 Q185 55 170 0 Z" fill="url(#rubber)" role="img" aria-label="Photo of black rubber expansion joints with steel flanges"/>
    <path d="M385 0 H590 Q605 55 640 108 H410 Q395 55 385 0 Z" fill="url(#braided)" role="img" aria-label="Photo of braided and composite hoses with flanged ends"/>
    <path d="M595 0 H848 V108 H645 Q610 55 595 0 Z" fill="url(#site)" role="img" aria-label="Photo of a braided hose installed on a gravel site"/>
  </svg>
</div>
</body>
</html>
```